Veterinary Business cards

Redesign Business Card

Information needed on Card:
Hours: Mon-Fri: 4pm -10PM; Sat- Sun- 10 AM- 5PM
Help@bayfernvet.com
www.bayfernvet.com
555-718-2946
4173 SE 19th Ave. okc, ok 73958
*No appointment necessary*

Optional:
Our tag line is "We're here when you need us" - If it fits on the cards.

```html
<!DOCTYPE html>
<html lang="en">
<head>
<meta charset="utf-8">
<title>Bayfern Vet Urgent Care – Business Card</title>
<link href="https://fonts.googleapis.com/css2?family=Roboto:wght@400;500;700&display=swap" rel="stylesheet">
<style>
  :root {
    --page: #2b2b2d;
    --orange: #d77a1b;
    --navy: #173a66;
    --white: #ffffff;
    --card-radius: 26px;
  }
  * { margin: 0; padding: 0; box-sizing: border-box; }
  html, body { width: 1200px; height: 960px; overflow: hidden; }
  body {
    background: var(--page);
    font-family: "Roboto", Arial, sans-serif;
    position: relative;
  }
  .card {
    position: absolute;
    left: 250px;
    width: 700px;
    height: 400px;
    border-radius: var(--card-radius);
    overflow: hidden;
  }
  .card--front { top: 60px; background: var(--orange); color: var(--navy); }
  .card--back { top: 500px; background: var(--navy); color: var(--white); }

  .brand-name {
    font-weight: 500; letter-spacing: 2px; text-transform: uppercase; white-space: nowrap;
  }

  /* front */
  .front-brand {
    position: absolute; left: 0; right: 0; top: 140px; text-align: center;
  }
  .front-brand .brand-name { font-size: 40px; }
  .front-brand .brand-rule {
    width: 340px; height: 2px; background: var(--navy); margin: 14px auto 0;
  }
  .tagline {
    position: absolute; left: 0; right: 0; top: 290px;
    text-align: center; font-size: 15px;
  }

  /* back */
  .back-brand {
    position: absolute; right: 44px; top: 36px; text-align: right;
  }
  .back-brand .brand-name { font-size: 26px; }
  .back-brand .brand-rule { height: 2px; background: var(--white); margin-top: 10px; }

  .hours {
    position: absolute; left: 52px; top: 120px;
    font-size: 15px; line-height: 1.45;
  }
  .hours-label { color: var(--orange); font-weight: 700; letter-spacing: .5px; }
  .hours-note { color: var(--orange); font-weight: 500; margin-top: 2px; }

  .address {
    position: absolute; right: 44px; top: 150px; text-align: right;
    font-size: 16px; line-height: 1.35; font-style: normal;
  }

  .connector {
    position: absolute; left: 52px; right: 44px; top: 222px;
    height: 2px; background: var(--orange);
  }

  .badge-dot {
    position: absolute; left: -22px; top: 262px;
    width: 50px; height: 50px; border-radius: 50%; background: var(--orange);
  }
  .person { position: absolute; left: 52px; top: 234px; }
  .person-name {
    color: var(--orange); font-size: 24px; font-weight: 700; letter-spacing: .5px;
  }
  .person-role { font-size: 17px; margin-top: 2px; }
  .person-rule {
    position: absolute; left: 52px; top: 296px; width: 230px;
    height: 2px; background: var(--orange);
  }

  .contact-list {
    position: absolute; left: 52px; top: 306px; list-style: none;
    font-size: 17px; line-height: 1.35;
  }
  .contact-list li { display: flex; align-items: center; gap: 10px; }
  .contact-list svg { width: 14px; height: 14px; flex: none; }
  .icon-fill { fill: var(--orange); }
  .icon-line { fill: none; stroke: var(--orange); stroke-width: 2.5; }
</style>
</head>
<body>

<section class="card card--front" aria-label="Card front">
  <div class="front-brand">
    <div class="brand-name">Bayfern Vet Urgent Care</div>
    <div class="brand-rule"></div>
  </div>
  <p class="tagline">We're here when you need us</p>
</section>

<section class="card card--back" aria-label="Card back">
  <div class="back-brand">
    <div class="brand-name">Bayfern Vet Urgent Care</div>
    <div class="brand-rule"></div>
  </div>

  <div class="hours">
    <div class="hours-label">HOURS</div>
    <div>Mon–Fri: 4 PM – 10 PM</div>
    <div>Sat–Sun: 10 AM – 5 PM</div>
    <div class="hours-note">*No appointment necessary*</div>
  </div>

  <address class="address">
    Bayfern Vet Urgent Care<br>
    4173 SE 19th Ave. okc<br>
    ok 73958
  </address>

  <div class="connector"></div>

  <div class="badge-dot"></div>
  <div class="person">
    <div class="person-name">DANIEL REYES</div>
    <div class="person-role">President</div>
  </div>
  <div class="person-rule"></div>

  <ul class="contact-list">
    <li>
      <svg viewBox="0 0 24 24"><path class="icon-fill" d="M6.6 10.8a15.1 15.1 0 0 0 6.6 6.6l2.2-2.2a1 1 0 0 1 1-.25 11.4 11.4 0 0 0 3.6.57 1 1 0 0 1 1 1V20a1 1 0 0 1-1 1A17 17 0 0 1 3 4a1 1 0 0 1 1-1h3.5a1 1 0 0 1 1 1c0 1.25.2 2.45.57 3.6a1 1 0 0 1-.25 1z"/></svg>
      555-718-2946
    </li>
    <li>
      <svg viewBox="0 0 24 24"><rect class="icon-line" x="2.5" y="5.5" width="19" height="13"/><path class="icon-line" d="M2.5 5.5l9.5 7.5 9.5-7.5"/></svg>
      Help@bayfernvet.com
    </li>
    <li>
      <svg viewBox="0 0 24 24"><circle class="icon-fill" cx="12" cy="12" r="10"/></svg>
      www.bayfernvet.com
    </li>
  </ul>
</section>

</body>
</html>
```